Cookbook - Book Cover Contest

Title: 40 Suppers Worth Sharing Around Town - A Neighborly Gratitude Kitchen Book
Dimensions: 8x5 x 8x5 inches
FRONT AND BACK COVER SEPARATE / NO SPINE
Final Formats: png, jpg, pdf, ai/vector + Layers & Fonts

Description:
I would like the part of the title that says "40 Suppers Worth Sharing Around Town" to be the main and bigger title and the smaller, secondary title "A Neighborly Gratitude Kitchen Book". I want to have a beautiful cover with the theme of teachers, school, chalkboard but I want it to be clear it is a cookbook. I want the title to be big and eye-catching, easy to read. The colors should be unisex, fun, and vibrant. Please do not make it too busy and hard to read. The cookbook is American style, so seafood and meat are included but please do not add your own pictures of food. I added two images, you're NOT required to use them as I do want a more chalkboard style cover to match the interior of the book.
I do NOT want real pictures of teachers or people on the cookbook cover.

If you have questions, please just let me know!

```html
<!DOCTYPE html>
<html lang="en">
<head>
<meta charset="utf-8">
<title>40 Suppers Worth Sharing Around Town - A Neighborly Gratitude Kitchen Book</title>
<link rel="stylesheet" href="https://fonts.googleapis.com/css2?family=Antonio:wght@100;400;700&display=swap">
<style>
  :root {
    --marble-light: #f4f1ee;
    --marble-mid: #e6dfd8;
    --wood-dark: #4a2a1c;
    --wood-mid: #6b3c26;
    --plate-rim: #3a3634;
    --plate-face: #c9bfb4;
    --dish-warm: #a4583a;
    --sauce: #9a3a22;
    --accent-orange: #d9762b;
    --accent-orange-soft: rgba(217, 118, 43, 0.8);
    --wood-tint: rgba(217, 118, 43, 0.35);
    --band-orange: rgba(217, 118, 43, 0.82);
    --author-panel: rgba(255, 255, 255, 0.85);
    --ink-white: #ffffff;
  }
  html, body {
    margin: 0;
    padding: 0;
    width: 1200px;
    height: 1198px;
    overflow: hidden;
    background: #ffffff;
  }
  .cover {
    position: relative;
    width: 1200px;
    height: 1198px;
    overflow: hidden;
  }
  .cover-art {
    position: absolute;
    inset: 0;
    display: block;
  }
  .title-number,
  .title-line,
  .subtitle,
  .author-label {
    font-family: "Antonio", "Arial Narrow", sans-serif;
  }
  .title-number { font-weight: 100; fill: var(--ink-white); }
  .title-line { font-weight: 400; fill: var(--ink-white); }
  .subtitle { font-weight: 400; fill: var(--ink-white); }
  .author-label { font-weight: 700; fill: var(--accent-orange); }
</style>
</head>
<body>
<main class="cover">
  <svg class="cover-art" width="1200" height="1198" viewBox="0 0 1200 1198" xmlns="http://www.w3.org/2000/svg">
    <defs>
      <linearGradient id="marbleTone" x1="0" y1="0" x2="1" y2="1">
        <stop offset="0" stop-color="var(--marble-light)"/>
        <stop offset="0.55" stop-color="var(--marble-mid)"/>
        <stop offset="1" stop-color="var(--marble-light)"/>
      </linearGradient>
      <linearGradient id="woodTone" x1="0" y1="0" x2="1" y2="0">
        <stop offset="0" stop-color="var(--wood-dark)"/>
        <stop offset="0.5" stop-color="var(--wood-mid)"/>
        <stop offset="1" stop-color="var(--wood-dark)"/>
      </linearGradient>
      <radialGradient id="mainDishTone" cx="0.5" cy="0.5" r="0.5">
        <stop offset="0" stop-color="var(--dish-warm)"/>
        <stop offset="0.85" stop-color="var(--plate-face)"/>
        <stop offset="1" stop-color="var(--plate-rim)"/>
      </radialGradient>
      <radialGradient id="sideDishTone" cx="0.5" cy="0.5" r="0.5">
        <stop offset="0" stop-color="#5a2a22"/>
        <stop offset="0.85" stop-color="var(--plate-face)"/>
        <stop offset="1" stop-color="var(--plate-rim)"/>
      </radialGradient>
      <radialGradient id="sauceTone" cx="0.5" cy="0.5" r="0.5">
        <stop offset="0" stop-color="var(--sauce)"/>
        <stop offset="0.8" stop-color="#b9552f"/>
        <stop offset="1" stop-color="#e9e4df"/>
      </radialGradient>
    </defs>

    <g class="food-photo">
      <rect class="marble-surface" x="0" y="0" width="1200" height="1198" fill="url(#marbleTone)" role="img" aria-label="White marble countertop with warm orange veins"/>
      <rect class="wood-board" x="334" y="0" width="150" height="1198" fill="url(#woodTone)" role="img" aria-label="Dark wooden serving board"/>
      <circle class="side-dish" cx="1169" cy="522" r="271" fill="url(#sideDishTone)" role="img" aria-label="Plate of grilled meat salad with greens and red onion"/>
      <circle class="main-dish" cx="626" cy="689" r="418" fill="url(#mainDishTone)" role="img" aria-label="Bowl of sliced steak, lettuce and shrimp in curry sauce with red chili"/>
      <circle class="sauce-bowl" cx="136" cy="939" r="115" fill="url(#sauceTone)" role="img" aria-label="Small glass bowl of red chili dipping sauce"/>
    </g>

    <rect class="wood-tint" x="334" y="0" width="150" height="1198" fill="var(--wood-tint)"/>
    <rect class="title-panel" x="484" y="0" width="518" height="553" fill="var(--accent-orange-soft)"/>
    <text class="title-number" x="46" y="449" font-size="475" textLength="392" lengthAdjust="spacingAndGlyphs">40</text>
    <text class="title-line title-line--lead" x="532" y="198" font-size="160" textLength="448" lengthAdjust="spacingAndGlyphs">SUPPERS</text>
    <text class="title-line" x="532" y="355" font-size="125" textLength="448" lengthAdjust="spacingAndGlyphs">WORTH SHARING</text>
    <text class="title-line" x="532" y="500" font-size="112" textLength="440" lengthAdjust="spacingAndGlyphs">AROUND TOWN</text>

    <rect class="subtitle-band" x="0" y="752" width="1200" height="84" fill="var(--band-orange)"/>
    <text class="subtitle" x="108" y="815" font-size="50" textLength="977" lengthAdjust="spacingAndGlyphs">A NEIGHBORLY GRATITUDE KITCHEN BOOK</text>

    <rect class="author-bar" x="772" y="968" width="17" height="122" fill="var(--accent-orange)"/>
    <rect class="author-panel" x="789" y="975" width="381" height="110" fill="var(--author-panel)"/>
    <text class="author-label" x="872" y="1062" font-size="92" textLength="234" lengthAdjust="spacingAndGlyphs">AUTHOR</text>
  </svg>
</main>
</body>
</html>
```